Work Van Graphics Design

Use the attached logo and design a work van.  The van should be orange (the same orange in the attached logo) and the logo and text will be white.  I want the text to be big and bold, the same hight as the graphic in the logo.  The text should be "BRAMLEY HOUSE CREW'S" instead of just Bramley.
The other text that needs to be on the van somewhere:
www.BramleyHouseCrews.example
555-281-9376
Roofing
Plumbing
Water Restoration
Carpet Cleaning
Window Cleaning
HVAC

```html
<!DOCTYPE html>
<html lang="en">
<head>
<meta charset="utf-8">
<title>Bramley House Crew's – Work Van Graphics</title>
<link href="https://fonts.googleapis.com/css2?family=Oswald:wght@600&family=Montserrat:wght@700&family=Saira+Semi+Condensed:wght@600&display=swap" rel="stylesheet">
<style>
  :root {
    --backdrop: #ecebe8;
    --van-orange: #e67a22;
    --van-orange-shade: #cf6a18;
    --wrap-white: #ffffff;
    --ink: #1c1c1c;
    --glass: #2b2b2d;
    --tyre: #1f1f1f;
    --rim: #bfc1c3;
    --panel-line: #b95d12;
  }
  html, body {
    margin: 0;
    padding: 0;
    width: 1200px;
    height: 675px;
    overflow: hidden;
    background: var(--backdrop);
  }
  .van-artboard { display: block; width: 1200px; height: 675px; }
  .van-body { fill: var(--van-orange); }
  .van-glass { fill: var(--glass); }
  .panel-seam { stroke: var(--panel-line); stroke-width: 1.2; fill: none; }
  .tyre { fill: var(--tyre); }
  .rim { fill: var(--rim); }
  .bumper { fill: var(--ink); }
  .info-stripe { fill: var(--wrap-white); }
  .brand-name {
    font-family: 'Oswald', sans-serif;
    font-weight: 600;
    fill: var(--wrap-white);
  }
  .brand-square { fill: var(--wrap-white); }
  .web-address {
    font-family: 'Montserrat', sans-serif;
    font-weight: 700;
    font-size: 14px;
    letter-spacing: 0.6px;
    fill: var(--ink);
  }
  .phone-number {
    font-family: 'Montserrat', sans-serif;
    font-weight: 700;
    font-size: 15px;
    letter-spacing: 1px;
    fill: var(--ink);
  }
  .stripe-icon { fill: var(--van-orange); }
  .service-item {
    font-family: 'Saira Semi Condensed', sans-serif;
    font-weight: 600;
    font-size: 12.5px;
    fill: var(--wrap-white);
  }
  .service-bullet { fill: var(--wrap-white); }
  .illustration-slot { fill: var(--van-orange-shade); }
</style>
</head>
<body>
<svg class="van-artboard" viewBox="0 0 1200 675" xmlns="http://www.w3.org/2000/svg">
  <!-- Van side panel -->
  <path class="van-body" d="M222 436 L214 350 Q214 318 244 308 L398 283 Q410 281 418 272 L472 210 Q480 200 494 199 L958 196 Q972 196 974 212 L976 420 Q976 432 964 432 L222 436 Z"/>
  <rect class="bumper" x="211" y="392" width="22" height="44" rx="3"/>
  <rect class="bumper" x="968" y="388" width="26" height="30" rx="3"/>

  <!-- Cab window -->
  <path class="van-glass" d="M436 292 L476 228 Q482 218 494 218 L552 216 Q560 216 560 224 L560 286 Q560 294 552 294 Z"/>

  <!-- Door seams -->
  <path class="panel-seam" d="M414 290 L414 428 M574 210 L574 426 M757 198 L757 424"/>

  <!-- Service illustration area -->
  <g role="img" aria-label="Isometric line illustration of a house cutaway with pipes">
    <polygon class="illustration-slot" points="848,198 880,198 968,240 968,262 890,316 800,316"/>
  </g>

  <!-- Brand name -->
  <rect class="brand-square" x="606" y="234" width="22" height="22"/>
  <text class="brand-name" x="640" y="262" font-size="38">BRAMLEY</text>
  <text class="brand-name" x="640" y="294" font-size="27">HOUSE CREW'S</text>

  <!-- Info stripe -->
  <polygon class="info-stripe" points="298,322 948,316 936,340 284,348"/>
  <circle class="stripe-icon" cx="349" cy="336" r="6"/>
  <text class="web-address" x="373" y="341">www.BramleyHouseCrews.example</text>
  <circle class="stripe-icon" cx="716" cy="330" r="6.5"/>
  <path d="M713.5 327 q0.5 4 5 5.5 l1-1.4 -1.8-1 -0.8 0.8 q-1.6-0.8-2.2-2.2 l0.8-0.8 -1-1.8 Z" fill="#ffffff"/>
  <text class="phone-number" x="742" y="336">555-281-9376</text>

  <!-- Services -->
  <g class="services">
    <circle class="service-bullet" cx="471" cy="373" r="1.6"/>
    <text class="service-item" x="480" y="377">Roofing</text>
    <circle class="service-bullet" cx="471" cy="388" r="1.6"/>
    <text class="service-item" x="480" y="392">Plumbing</text>
    <circle class="service-bullet" cx="471" cy="403" r="1.6"/>
    <text class="service-item" x="480" y="407">Water Restoration</text>

    <circle class="service-bullet" cx="616" cy="369" r="1.6"/>
    <text class="service-item" x="624" y="373">Carpet Cleaning</text>
    <circle class="service-bullet" cx="616" cy="384" r="1.6"/>
    <text class="service-item" x="624" y="388">Window Cleaning</text>
    <circle class="service-bullet" cx="616" cy="400" r="1.6"/>
    <text class="service-item" x="624" y="404">HVAC</text>
  </g>

  <!-- Wheels -->
  <circle class="tyre" cx="336" cy="425" r="52"/>
  <circle class="rim" cx="336" cy="425" r="32"/>
  <circle class="tyre" cx="829" cy="428" r="52"/>
  <circle class="rim" cx="829" cy="428" r="32"/>
</svg>
</body>
</html>
```